Simple : A Therapist is looking for a Design

Im lookind for a business card design for my new business .
my therapy field - Interactive Craniosacral .
Its part of Osteopatic medicine .
its gental, not invasive method that focus on the bones of the skull (cranial) .
i want some kind of skull in it like the attached photo.

Target Market(s)

people that suffer from pain

Industry/Entity Type

Physical Therapy

Contact Information for Business Card

i want people to understand this is diffrent kind of therapy
its anatomy base , gental and give outstanding result .

Font styles to use
Serif

Colors
fee18a
cadf82
fbc994
cedeed
fbe7d2
fff3d1

Requirements
Must have
• one side: my name (Yoram Shefet) ,
• phone number ( 0521746098)
• email (shefetyoram@postvela.com)
• other side : Interactive Craniosacral
Nice to have
• i want some kind of skull in it like the attached photo.
• very powrful, accurate and smart.
• nice colores (maybe lite orange?, lite green?) , simple, relax, smart

```html
<!DOCTYPE html>
<html lang="en">
<head>
<meta charset="UTF-8">
<title>Gentle Cranial Balance – Business Card</title>
<link rel="stylesheet" href="https://fonts.googleapis.com/css2?family=Exo+2:wght@400;500&display=swap">
<style>
  :root {
    --page-bg: #e9e9e6;
    --card-green: #cadf82;
    --card-white: #ffffff;
    --brand-green: #c3dc7e;
    --brand-yellow: #fbdc86;
    --text-white: #ffffff;
    --circle-soft: #e6f0c4;
  }
  * { box-sizing: border-box; margin: 0; padding: 0; }
  html, body {
    width: 1200px;
    height: 800px;
    overflow: hidden;
    background: var(--page-bg);
    font-family: "Exo 2", sans-serif;
  }
  .canvas {
    width: 1200px;
    height: 800px;
    display: flex;
    flex-direction: column;
    align-items: center;
    justify-content: center;
    gap: 40px;
  }
  .card {
    width: 600px;
    height: 343px;
    position: relative;
    box-shadow: 0 6px 18px rgba(0,0,0,0.12);
  }
  .card--front {
    background: var(--card-green);
    display: flex;
    align-items: center;
    justify-content: center;
    gap: 18px;
  }
  .brand-dot {
    width: 34px;
    height: 34px;
    border-radius: 50%;
    background: var(--text-white);
  }
  .brand-name {
    font-weight: 500;
    line-height: 1;
  }
  .card--front .brand-name {
    color: var(--text-white);
    font-size: 38px;
    letter-spacing: 1px;
  }
  .card--back {
    background: var(--card-white);
  }
  .mark-circle {
    position: absolute;
    left: 70px;
    top: 80px;
    width: 190px;
    height: 190px;
    border-radius: 50%;
    background: var(--circle-soft);
  }
  .back-info {
    position: absolute;
    left: 300px;
    top: 95px;
  }
  .card--back .brand-name {
    color: var(--brand-green);
    font-size: 30px;
    letter-spacing: 0.5px;
  }
  .card--back .brand-name span { display: block; margin-bottom: 4px; }
  .person-name {
    margin-top: 18px;
    color: var(--brand-green);
    font-size: 17px;
    letter-spacing: 0.5px;
  }
  .contact-list {
    list-style: none;
    margin-top: 10px;
  }
  .contact-item {
    display: flex;
    align-items: center;
    gap: 8px;
    color: var(--brand-yellow);
    font-size: 14px;
    margin-top: 6px;
  }
  .contact-icon { width: 13px; height: 13px; flex: none; }
</style>
</head>
<body>
  <main class="canvas">
    <section class="card card--front" aria-label="Card front">
      <div class="brand-dot"></div>
      <div class="brand-name">Gentle Cranial Balance</div>
    </section>

    <section class="card card--back" aria-label="Card back">
      <div class="mark-circle"></div>
      <div class="back-info">
        <div class="brand-name"><span>Gentle Cranial</span><span>Balance</span></div>
        <p class="person-name">Yoram Shefet</p>
        <ul class="contact-list">
          <li class="contact-item">
            <svg class="contact-icon" viewBox="0 0 13 13" aria-hidden="true">
              <rect x="2.5" y="0.8" width="8" height="11.4" rx="1.5" fill="none" stroke="#c3dc7e" stroke-width="1.4"/>
              <line x1="5.5" y1="10" x2="7.5" y2="10" stroke="#c3dc7e" stroke-width="1.2"/>
            </svg>
            0521746098
          </li>
          <li class="contact-item">
            <svg class="contact-icon" viewBox="0 0 13 13" aria-hidden="true">
              <rect x="0.7" y="2.5" width="11.6" height="8" fill="#c3dc7e"/>
              <polyline points="0.7,2.5 6.5,7.2 12.3,2.5" fill="none" stroke="#ffffff" stroke-width="1.1"/>
            </svg>
            shefetyoram@postvela.com
          </li>
        </ul>
      </div>
    </section>
  </main>
</body>
</html>
```